Judicial election website to attract voters

I need a simple one-page web design for a judicial election. I'm going to put up one picture, maybe two. The picture I have needs a little touch-up (whiten teeth for example). I have 3 paragraphs of text. I'd like a "Donate" button that can link to a Tillwisp account. I'd also like a little background design, like the Constitution or something like that. There's a couple other little things but that's the bulk of it.

Target Market(s)

Involved voters and some media

Industry/Entity Type

Legal

Number of Pages Required

1 page

Font styles to use
Sans Serif

Requirements
Must have
• My picture, text, donate button
• Phrase "Remember to vote August 30, 2016!"
Nice to have
• Perhaps a second photo, maybe a short 30 second video of me talking directly to the voters, cool background: Constitution, something judgey.
Should not have
• Not sure ... profanity, I guess.

```html
<!DOCTYPE html>
<html lang="en">
<head>
<meta charset="utf-8">
<title>Marlena for Judge</title>
<link href="https://fonts.googleapis.com/css2?family=Bree+Serif&family=Hind:wght@400;500&family=Open+Sans:wght@400;600&display=swap" rel="stylesheet">
<style>
:root{
  --header-bg:rgba(52,52,52,.92);
  --white:#ffffff;
  --sky-light:#e6e7e8;
  --sky-mid:#c9ccd0;
  --dome-warm:#e9c9a0;
  --banner-cyan:#1ea3da;
  --banner-blue:#1a6fd6;
  --heading-blue:#2a5da8;
  --body-text:#666666;
  --button-blue-top:#2f6fc0;
  --button-blue-bottom:#1d4f96;
  --parchment:#ebe6df;
  --parchment-deep:#d9d1c5;
  --dark-text:#333333;
  --donate-top:#ffc21a;
  --donate-bottom:#ff9d00;
  --footer-blue:#1f4c9f;
  --footer-line:#163a80;
  --footer-text:#dfe6f4;
}
*{margin:0;padding:0;box-sizing:border-box}
html,body{width:1020px;height:1200px;overflow:hidden;background:var(--white)}
body{position:relative;font-family:"Open Sans",sans-serif}
.hero{position:absolute;left:0;top:0;width:1020px;height:474px;
  background:linear-gradient(100deg,var(--sky-light) 0%,var(--sky-mid) 45%,#d8cfc4 75%,var(--dome-warm) 100%)}
.site-header{position:absolute;left:0;top:0;width:1020px;height:71px;background:var(--header-bg)}
.brand{position:absolute;left:130px;top:10px;font-family:"Bree Serif",serif;font-size:35px;color:var(--white)}
.main-nav a{position:absolute;top:36px;font-family:"Hind",sans-serif;font-size:13.5px;color:var(--white);text-decoration:none;letter-spacing:.2px}
.main-nav .active::after{content:"";position:absolute;left:-3px;right:-3px;top:33px;height:2px;background:var(--white)}
.vote-line{position:absolute;left:131px;font-family:"Hind",sans-serif;font-weight:500;color:var(--white);padding-left:21px}
.vote-line.primary{top:218px;width:371px;height:48px;background:var(--banner-cyan);font-size:34px;line-height:54px}
.vote-line.secondary{top:268px;width:331px;height:44px;background:var(--banner-blue);font-size:27px;line-height:48px}
.slider-dots{position:absolute;left:470px;top:444px}
.intro-title{position:absolute;left:121px;top:513px;font-family:"Hind",sans-serif;font-weight:500;font-size:26px;color:var(--heading-blue);letter-spacing:.4px}
.portrait{position:absolute;left:124px;top:559px;width:216px;height:187px;background:linear-gradient(160deg,#d9d4cf,#c9a48a 60%,#d88a70)}
.portrait::after{content:"";position:absolute;left:6px;top:6px;right:8px;bottom:8px;border:2px solid var(--white)}
.bio{position:absolute;left:366px;width:510px;font-size:10.4px;line-height:18.2px;color:var(--body-text)}
.bio.first{top:561px}.bio.second{top:641px}
.btn-read{position:absolute;left:365px;top:714px;width:97px;height:30px;border-radius:3px;background:linear-gradient(var(--button-blue-top),var(--button-blue-bottom));color:var(--white);font-family:"Hind",sans-serif;font-size:11.5px;text-align:center;line-height:32px}
.video-band{position:absolute;left:0;top:789px;width:1020px;height:297px;background:linear-gradient(90deg,var(--parchment-deep),var(--parchment) 35%,var(--parchment) 100%)}
.video-title{position:absolute;left:126px;top:835px;font-family:"Hind",sans-serif;font-size:25px;color:var(--dark-text)}
.video-copy{position:absolute;left:129px;width:445px;font-size:10.4px;line-height:18.4px;color:var(--body-text)}
.video-copy.first{top:880px}.video-copy.second{top:946px}
.btn-donate{position:absolute;left:130px;top:995px;width:97px;height:30px;border-radius:2px;background:linear-gradient(var(--donate-top),var(--donate-bottom));color:var(--white);font-family:"Hind",sans-serif;font-weight:500;font-size:12px;text-align:center;line-height:32px}
.video-frame{position:absolute;left:593px;top:840px;width:309px;height:196px;background:var(--white);box-shadow:0 1px 3px rgba(0,0,0,.2)}
.video-still{position:absolute;left:5px;top:6px;width:299px;height:161px;background:linear-gradient(120deg,#2c3f66 0%,#8a6a3a 40%,#caa060 65%,#7c2a2a 100%)}
.video-controls{position:absolute;left:5px;top:167px;width:299px;height:23px;background:#1f1f1f}
.site-footer{position:absolute;left:0;top:1086px;width:1020px;height:114px;background:var(--footer-blue);border-top:3px solid var(--footer-line)}
.footer-nav a{position:absolute;top:28px;font-family:"Hind",sans-serif;font-size:12.5px;color:var(--footer-text);text-decoration:none}
.copyright{position:absolute;left:0;width:1020px;top:50px;text-align:center;font-size:9.5px;color:var(--footer-text);padding-left:-20px}
.social{position:absolute;left:441px;top:71px}
</style>
</head>
<body>
<div class="hero" role="img" aria-label="Photograph of a domed capitol building with a flag under a cloudy sky"></div>

<header class="site-header">
  <div class="brand">Marlena</div>
  <nav class="main-nav">
    <a class="active" style="left:415px">HOME</a>
    <a style="left:492px">ABOUT</a>
    <a style="left:574px">VIDEO</a>
    <a style="left:652px">DONATE</a>
    <a style="left:742px">BLOG</a>
    <a style="left:816px">CONTACT</a>
  </nav>
</header>

<div class="vote-line primary">REMEMBER TO VOTE</div>
<div class="vote-line secondary">AUGUST 30, 2016</div>

<svg class="slider-dots" width="80" height="16" viewBox="0 0 80 16">
  <circle cx="7" cy="8" r="6" fill="none" stroke="#fff" stroke-width="1.6"/>
  <circle cx="24" cy="8" r="7" fill="#fff"/>
  <circle cx="42" cy="8" r="7" fill="#fff"/>
  <circle cx="60" cy="8" r="7" fill="#fff"/>
</svg>

<h2 class="intro-title">EXPERIENCED . DEDICATED . RESPECTED</h2>
<div class="portrait" role="img" aria-label="Portrait photograph of the candidate"></div>
<p class="bio first">Marlena was born and raised in Tampa Florida, the daughter of an air-conditioning repairman who later opened his own successful business. As the first in her family to go to college, her parents could not have been more proud as she finished her degree at Palmetto State University, then continued on to Coral Bay School of Law where she graduated with honors.</p>
<p class="bio second">Dedicating her life to public service in central Florida, she has spent the last 18 years as a prosecutor fighting for victims of child abuse and sexual abuse in Orange and Osceola counties. She participates in local charities such as the Harvest Table Pantry and the Open Page Reading Circle.</p>
<div class="btn-read">READ MORE</div>

<section class="video-band" role="img" aria-label="Faded background of an old parchment constitution with quill and inkwell"></section>
<h2 class="video-title">Watch Latest Video</h2>
<p class="video-copy first">The cornerstone of Marlena's candidacy for judge is her experience in the courtroom. Nobody knows how to run an efficient courtroom better than an attorney who has litigated a hundred felony jury trials and argued more pretrial motions than can be counted.</p>
<p class="video-copy second">But even a judge with all the right knowledge and experience cannot excel without the correct temperament. Ask any attorney or judge who has worked with Marlena</p>
<div class="btn-donate">DONATE</div>

<div class="video-frame">
  <div class="video-still" role="img" aria-label="Video still of a parchment constitution scroll on a flag"></div>
  <svg style="position:absolute;left:135px;top:68px" width="30" height="30" viewBox="0 0 30 30">
    <circle cx="15" cy="15" r="15" fill="#fff"/>
    <path d="M11 8 L22 15 L11 22 Z" fill="#111"/>
  </svg>
  <div class="video-controls">
    <svg width="299" height="23" viewBox="0 0 299 23">
      <path d="M10 6 L19 11.5 L10 17 Z" fill="#fff"/>
      <rect x="29" y="9" width="202" height="5" rx="2.5" fill="#e8e8e8"/>
      <rect x="29" y="9" width="80" height="5" rx="2.5" fill="#3d7fd8"/>
      <path d="M276 9 h3 l4 -3 v11 l-4 -3 h-3 Z" fill="#fff"/>
      <path d="M285 8 q3 3.5 0 7" stroke="#fff" stroke-width="1.2" fill="none"/>
    </svg>
  </div>
</div>

<footer class="site-footer">
  <nav class="footer-nav">
    <a style="left:289px">HOME</a>
    <a style="left:358px">ABOUT</a>
    <a style="left:432px">VIDEO</a>
    <a style="left:502px">DONATE</a>
    <a style="left:583px">BLOG</a>
    <a style="left:649px">CONTACT</a>
  </nav>
  <p class="copyright">© 2016 Company Name&nbsp; All right reserved</p>
  <svg class="social" width="112" height="28" viewBox="0 0 112 28" role="img" aria-label="Social links">
    <circle cx="14" cy="14" r="12" fill="none" stroke="#fff" stroke-width="1.4"/>
    <circle cx="41" cy="14" r="12" fill="none" stroke="#fff" stroke-width="1.4"/>
    <circle cx="69" cy="14" r="12" fill="none" stroke="#fff" stroke-width="1.4"/>
    <circle cx="97" cy="14" r="12" fill="none" stroke="#fff" stroke-width="1.4"/>
  </svg>
</footer>
</body>
</html>
```